Web page for analytics company

Now that I have a new logo, I need a webpage design that will use it to its potential. Am looking for a design that handles presentation and access to data well - like sites with blocks that provide direct access to content without going through a set of menus. More like an infographic. No left/right menu bar.

I want the logo (attached) against a black background, but not text - not a fan of trying to read white text on a dark screen.

The website - torvimbly.com - currently has four pages - home, who we are, by the numbers and a blog.

The site will be done in Squarespace.

My apologies for not responding promptly - big report due today.  I will be online tomorrow with answers and feedback. 

Thanks!

```html
<!DOCTYPE html>
<html lang="en">
<head>
<meta charset="utf-8">
<title>Torvimbly – Gender Equity Analytics</title>
<link href="https://fonts.googleapis.com/css2?family=Lato:wght@300;400;700;900&display=swap" rel="stylesheet">
<style>
:root{
  --black:#050505;
  --orange:#f7941d;
  --green:#8fd4a9;
  --red:#f47a7a;
  --lime:#a8d07f;
  --band:#ebebed;
  --section:#f0f0f2;
  --text:#555;
  --muted:#8a8a8a;
  --dark:#2b2b2b;
  --white:#fff;
  --line:#d8d8d8;
}
*{box-sizing:border-box;margin:0;padding:0}
html,body{width:1200px;height:2740px;overflow:hidden}
body{font-family:'Lato',sans-serif;background:var(--white);color:var(--text);position:relative}
.abs{position:absolute}

/* header */
.site-header{left:0;top:0;width:1200px;height:91px;background:var(--black)}
.brand{left:104px;top:18px;display:flex;align-items:center;gap:12px;color:var(--white);font-size:36px;font-weight:400}
.brand-dot{width:52px;height:52px;border-radius:50%;background:var(--orange)}
.menu-icon{left:1052px;top:32px}

/* hero */
.hero{left:0;top:91px;width:1200px;height:402px}
.hero-photo{left:0;top:0;width:1200px;height:402px;background:linear-gradient(90deg,#d2cdc6 0%,#b3a999 40%,#7a6a58 70%,#4b3d30 100%)}
.hero-title{left:592px;top:100px;color:var(--white);font-weight:900;font-size:44px;line-height:46px;letter-spacing:-1px;text-shadow:0 2px 6px rgba(0,0,0,.4)}
.hero-sub{left:594px;top:196px;color:var(--white);font-weight:700;font-size:17px;text-shadow:0 1px 4px rgba(0,0,0,.5)}
.btn-start{left:592px;top:238px;width:196px;height:46px;background:var(--orange);color:var(--white);font-weight:700;font-size:24px;display:flex;align-items:center;justify-content:center}

/* feature cards */
.card{top:511px;width:325px;height:185px;color:var(--white);padding:26px 24px 0 96px}
.card svg{position:absolute;left:16px;top:24px}
.card h3{font-weight:400;font-size:23px;color:#333;margin-bottom:8px}
.card .kicker{font-weight:700;font-size:12px;margin-bottom:10px}
.card p{font-size:12px;line-height:19px;color:#3e3e3e}
.card .more{display:inline-block;margin-top:10px;border:1px solid var(--white);font-size:9px;padding:2px 18px}
.card-articles{left:102px;background:var(--green)}
.card-meetings{left:438px;background:var(--red)}
.card-events{left:774px;background:var(--lime)}

/* section bands */
.band{left:100px;width:1000px;height:70px;background:var(--band);font-size:24px;color:var(--dark);padding-left:16px;display:flex;align-items:center}
.band::after{content:"";position:absolute;left:80px;bottom:-16px;border:16px solid transparent;border-top-color:var(--band);border-bottom:0}
.band-analytics{top:710px;font-weight:400;letter-spacing:.5px}
.band-testi{top:1603px;font-weight:700}
.band-mail{top:1956px;font-weight:700}

/* profile */
.profile{left:100px;top:813px;width:1000px;height:226px;border:2px solid #e1e1e1;border-radius:4px}
.profile-photo{left:18px;top:26px;width:128px;height:168px;background:linear-gradient(160deg,#8f6a4e,#3c2e26)}
.profile-name{left:168px;top:26px;color:var(--orange);font-weight:700;font-size:14px}
.profile-text{left:168px;top:52px;width:800px;font-size:12px;line-height:19px;color:#777}
.profile-more{left:168px;top:176px;border:1px solid var(--orange);color:var(--orange);font-size:9px;padding:3px 14px}

/* blog */
.blog{left:0;top:1070px;width:1200px;height:506px;background:var(--section)}
.blog-title{left:114px;top:36px;font-size:23px;color:#444}
.see-all{left:1038px;top:30px;font-size:20px;color:#555;text-decoration:underline}
.post{background:var(--white)}
.post .cat{font-size:9px;color:#999;text-transform:uppercase}
.post h4{font-weight:400;font-size:19px;color:#666;line-height:28px;margin-top:8px}
.post .meta{font-size:9px;color:#999;text-transform:uppercase}
.post-a{left:100px;top:80px;width:417px;height:148px;padding:16px 20px}
.post-a-img{left:100px;top:228px;width:417px;height:234px;background:linear-gradient(180deg,#d6d8db,#6f6d6b)}
.post-b{left:679px;top:80px;width:418px;height:142px;padding:16px 20px}
.post-b-img{left:275px;top:0;width:143px;height:142px;background:linear-gradient(135deg,#fafafa,#ececec);border-right:3px solid #e23a2c}
.post-c{left:679px;top:253px;width:418px;height:217px}
.post-c-img{left:0;top:0;width:139px;height:217px;background:linear-gradient(180deg,#b7b9bd,#6a5f58)}
.post-c-body{left:155px;top:16px;width:245px}
.post-c-body p{font-size:12px;line-height:19px;color:#888;margin-top:10px}
.timeline{left:597px;top:80px;width:1px;height:390px;background:var(--line)}
.tl-month{left:562px;top:52px;width:70px;height:70px;border-radius:50%;background:var(--white);text-align:center;font-size:12px;font-weight:700;color:#444;padding-top:22px;line-height:16px}
.tl-dot{width:40px;height:40px;border-radius:50%;background:var(--white);font-size:13px;color:#444;display:flex;align-items:center;justify-content:center}
.tl-link{height:1px;background:var(--line)}

/* testimonials */
.testi-name{font-weight:400;font-size:23px;color:#444}
.testi-text{font-size:15px;line-height:20px;color:#888;width:330px;margin-top:10px}
.testi-more{font-size:15px;color:#333;text-decoration:underline;margin-top:10px;display:block}
.avatar{width:124px;height:124px;border-radius:50%;border:4px solid var(--white);box-shadow:0 2px 6px rgba(0,0,0,.25)}

/* mailing */
.field{left:100px;width:517px;height:55px;background:var(--band);font-size:15px;color:#888;padding-left:18px;display:flex;align-items:center}
.btn-sub{left:100px;top:2255px;width:154px;height:53px;background:var(--orange);color:var(--white);font-size:20px;font-weight:700;display:flex;align-items:center;justify-content:center}
.connect-title{left:667px;top:2050px;font-size:23px;color:#333}
.connect-text{left:671px;top:2084px;width:400px;font-size:15px;line-height:26px;color:#888}
.social{top:2200px;width:66px;height:66px;border-radius:50%;background:#dcdcdc;border:2px solid #e8e8e8}
.btn-join{left:670px;top:2286px;width:402px;height:57px;background:var(--orange);color:var(--white);font-size:22px;display:flex;align-items:center;justify-content:center}

/* footer */
.footer{left:0;top:2361px;width:1200px;height:327px;background:linear-gradient(90deg,#e5e5e5,#f6f6f6 50%,#e5e5e5)}
.footer-bar{left:96px;top:13px;width:1008px;height:44px;background:var(--white);opacity:.7}
.footer-h{top:26px;font-size:14px;font-weight:700;color:#222}
.news{left:124px;width:340px}
.news .thumb{position:absolute;left:0;top:0;width:48px;height:40px;background:linear-gradient(135deg,#7aa3c7,#c9b59a)}
.news p{margin-left:68px;font-size:15px;line-height:21px;color:#555;border-bottom:1px solid #ccc;padding-bottom:4px}
.news small{display:block;margin-left:68px;font-size:9px;color:#999;margin-top:6px}
.comment{left:524px;width:250px}
.comment svg{position:absolute;left:0;top:4px}
.comment .who{margin-left:38px;font-size:12px;color:#555}
.comment .what{margin-left:38px;font-size:14px;color:#555;margin-top:6px;border-bottom:1px solid #ccc;padding-bottom:6px}
.contact-row{left:842px;font-size:11px;color:#666;letter-spacing:.5px}
.contact-row span{position:absolute;left:92px;white-space:nowrap;font-size:11px;letter-spacing:0}
.contact-row a{color:#2f7fc1;text-decoration:none}
.btn-contact{left:842px;top:2582px;width:258px;height:40px;background:var(--orange);color:var(--white);font-size:12px;font-weight:700;display:flex;align-items:center;padding-left:68px}
.btn-contact i{position:absolute;right:0;top:0;width:38px;height:40px;border-left:1px solid #fbb;display:flex;align-items:center;justify-content:center;font-style:normal;font-size:16px}
.bottom-bar{left:0;top:2688px;width:1200px;height:52px;background:#ddd}
.bottom-nav{left:108px;top:20px;font-size:12px;color:#555;word-spacing:2px}
.copyright{left:807px;top:20px;font-size:12px;color:#777}
</style>
</head>
<body>

<header class="site-header abs">
  <div class="brand abs"><span class="brand-dot"></span>Torvimbly</div>
  <svg class="menu-icon abs" width="30" height="28" viewBox="0 0 30 28"><rect y="0" width="30" height="6" fill="#fff"/><rect y="11" width="30" height="6" fill="#fff"/><rect y="22" width="30" height="6" fill="#fff"/></svg>
</header>

<section class="hero abs">
  <div class="hero-photo abs" role="img" aria-label="Hero photo of a smiling businesswoman with a thought bubble in a blurred office"></div>
  <h1 class="hero-title abs">GENDER<br>EQUITY ANALYTICS</h1>
  <div class="hero-sub abs">ENHANCING PERFORMANCE THROUGH A GENDER LENS</div>
  <div class="btn-start abs">Get Start</div>
</section>

<article class="card card-articles abs">
  <svg width="64" height="64" viewBox="0 0 64 64"><polygon points="32,4 40,24 62,25 45,39 51,60 32,48 13,60 19,39 2,25 24,24" fill="none" stroke="#fff" stroke-width="4" stroke-linejoin="round"/></svg>
  <h3>Articles &amp; Analytics</h3>
  <div class="kicker">Fact-sheet: EU-Ukraine relations</div>
  <p>Marta Lindqvist has over 30 years<br>of experience with gender equity<br>analytics, strategic analysis and</p>
  <span class="more">See Full</span>
</article>
<article class="card card-meetings abs">
  <svg width="64" height="64" viewBox="0 0 64 64"><rect x="6" y="22" width="20" height="32" rx="8" fill="#fff"/><rect x="38" y="22" width="20" height="32" rx="8" fill="#fff"/><rect x="10" y="8" width="12" height="16" rx="3" fill="#fff"/><rect x="42" y="8" width="12" height="16" rx="3" fill="#fff"/><rect x="24" y="28" width="16" height="8" fill="#fff"/></svg>
  <h3>Previous Meetings</h3>
  <div class="kicker">Fact-sheet: EU-Ukraine relations</div>
  <p>Marta Lindqvist has over 30 years<br>of experience with gender equity<br>analytics, strategic analysis and</p>
  <span class="more">See Full</span>
</article>
<article class="card card-events abs">
  <svg width="64" height="64" viewBox="0 0 64 64"><rect x="6" y="22" width="52" height="12" fill="none" stroke="#fff" stroke-width="4"/><rect x="10" y="34" width="44" height="24" fill="none" stroke="#fff" stroke-width="4"/><line x1="32" y1="22" x2="32" y2="58" stroke="#fff" stroke-width="4"/><path d="M32 22 C24 6 12 12 20 22 M32 22 C40 6 52 12 44 22" fill="none" stroke="#fff" stroke-width="4"/></svg>
  <h3>Upcoming Events</h3>
  <div class="kicker">Fact-sheet: EU-Ukraine relations</div>
  <p>Marta Lindqvist has over 30 years<br>of experience with gender equity<br>analytics, strategic analysis and</p>
  <span class="more">See Full</span>
</article>

<h2 class="band band-analytics abs">GENDER EQUITY ANALYTICS</h2>

<section class="profile abs">
  <div class="profile-photo abs" role="img" aria-label="Portrait photo of Marta Lindqvist"></div>
  <div class="profile-name abs">MARTA LINDQVIST</div>
  <p class="profile-text abs">As much as we'd like to think that treating everyone equally is the best strategy for fairness, the reality is that the differences in the lives of women and men have to be taken into account to ensure that organizations, programs, services, and yes, even public policy treat women and men in ways that achieve gender equity.<br>That's where Torvimbly - Gender Equity Analytics - comes in. Using the data-driven tools of gender analysis, we can help you determine if gender equity is being achieved - in businesses and organizations, in the planning and implementation of programs and services, and in the</p>
  <span class="profile-more abs">See Full</span>
</section>

<section class="blog abs">
  <h2 class="blog-title abs" style="font-weight:400">BLOG</h2>
  <span class="see-all abs">See All</span>

  <div class="timeline abs"></div>
  <div class="tl-link abs" style="left:517px;top:160px;width:60px"></div>
  <div class="tl-link abs" style="left:617px;top:216px;width:62px"></div>
  <div class="tl-month abs">MARCH<br><span style="font-weight:400">2014</span></div>
  <div class="tl-dot abs" style="left:577px;top:140px">1</div>
  <div class="tl-dot abs" style="left:577px;top:196px">2</div>
  <div class="tl-dot abs" style="left:577px;top:379px">3</div>

  <article class="post post-a abs">
    <div class="cat">Company</div>
    <h4>Council on Equity<br>A better world through a gendeR</h4>
    <div class="meta" style="margin-top:22px">3 Comments</div>
    <svg class="abs" style="right:18px;bottom:18px" width="18" height="14" viewBox="0 0 18 14"><path d="M10 0 L18 7 L10 14 V9 C5 9 2 11 0 14 C1 8 4 5 10 5Z" fill="#666"/></svg>
  </article>
  <div class="post-a-img abs" role="img" aria-label="Photo of a smiling business team of four"></div>

  <article class="post post-b abs">
    <div class="cat">Company</div>
    <h4>Council on Equity<br>A better world through</h4>
    <div class="meta" style="margin-top:22px">5 Comments</div>
    <svg class="abs" style="left:230px;bottom:18px" width="18" height="14" viewBox="0 0 18 14"><path d="M10 0 L18 7 L10 14 V9 C5 9 2 11 0 14 C1 8 4 5 10 5Z" fill="#666"/></svg>
    <div class="post-b-img abs" role="img" aria-label="Illustration of a red gender symbol"></div>
  </article>

  <article class="post post-c abs">
    <div class="post-c-img abs" role="img" aria-label="Photo of a young woman standing outdoors"></div>
    <div class="post-c-body abs">
      <div class="cat">Company</div>
      <h4>Council on Equity<br>A better world through</h4>
      <p>Swedish video closes the gender pay gap in 47 seconds: we just need to "be a man</p>
      <div class="meta" style="margin-top:46px;border-top:1px solid #ddd;padding-top:8px">5 Comments</div>
    </div>
    <svg class="abs" style="right:18px;bottom:18px" width="18" height="14" viewBox="0 0 18 14"><path d="M10 0 L18 7 L10 14 V9 C5 9 2 11 0 14 C1 8 4 5 10 5Z" fill="#666"/></svg>
  </article>
</section>

<h2 class="band band-testi abs">Testimonials</h2>

<div class="abs" style="left:134px;top:1736px">
  <div class="testi-name">MARTA LINDQVIST</div>
  <p class="testi-text">Lindqvist is a recognized expert on women in leadership in business and government as well as women's economic empowerment. She is an experienced qualitative researcher, and respec-</p>
  <span class="testi-more">Read aMore</span>
</div>
<div class="avatar abs" style="left:492px;top:1714px;background:linear-gradient(160deg,#9a7a62,#3e3430)" role="img" aria-label="Portrait photo of a woman"></div>
<div class="avatar abs" style="left:565px;top:1792px;background:linear-gradient(160deg,#b89a80,#5a4a40)" role="img" aria-label="Portrait photo of a man"></div>
<div class="abs" style="left:733px;top:1752px">
  <div class="testi-name">Lorem Ipsum</div>
  <p class="testi-text">Lindqvist is a recognized expert on women in leadership in business and government as well as women's economic empowerment. She is an experienced qualitative researcher, and respec-</p>
  <span class="testi-more">Read aMore</span>
</div>

<h2 class="band band-mail abs">Subcribe To Our Mailing List</h2>

<div class="field abs" style="top:2049px">Email Address......</div>
<div class="field abs" style="top:2116px">First Name</div>
<div class="field abs" style="top:2182px">Last Name</div>
<div class="btn-sub abs">SUBSCRIBE</div>

<h3 class="connect-title abs" style="font-weight:400">Connect With Your Friends Online</h3>
<p class="connect-text abs">The way we communicate has changed and social networks are now the center of our daily lives. We update our friends too).</p>
<div class="social abs" style="left:686px"></div>
<div class="social abs" style="left:779px"></div>
<div class="social abs" style="left:876px"></div>
<div class="social abs" style="left:969px"></div>
<div class="btn-join abs">JOIN US</div>

<footer class="footer abs">
  <div class="footer-bar abs"></div>
  <div class="footer-h abs" style="left:124px">Council on Equity</div>
  <div class="footer-h abs" style="left:524px">Comments</div>
  <div class="footer-h abs" style="left:840px">Contact Us</div>

  <div class="news abs" style="top:80px"><div class="thumb" role="img" aria-label="News thumbnail photo"></div><p>Swedish video closes the gender pay gap in 47 seconds: we just need to "</p><small>about a day ago</small></div>
  <div class="news abs" style="top:170px"><div class="thumb" role="img" aria-label="News thumbnail photo"></div><p>Halvorsen describes life-stage approach Norbelt Ltd. takes to women's</p><small>5 day ago</small></div>
  <div class="news abs" style="top:252px"><div class="thumb" role="img" aria-label="News thumbnail photo"></div><p>Need to stop using "choices" as an excuse for gender inequality</p><small>about a day ago</small></div>

  <div class="comment abs" style="top:84px"><svg width="22" height="20" viewBox="0 0 22 20"><path d="M0 0H22V14H8L3 19V14H0Z" fill="#aaa"/></svg><div class="who">Council on Equity</div><div class="what">Swedish video closes the gender</div></div>
  <div class="comment abs" style="top:164px"><svg width="22" height="20" viewBox="0 0 22 20"><path d="M0 0H22V14H8L3 19V14H0Z" fill="#aaa"/></svg><div class="who">Council on Equity</div><div class="what">Swedish video closes the gender</div></div>
  <div class="comment abs" style="top:244px"><svg width="22" height="20" viewBox="0 0 22 20"><path d="M0 0H22V14H8L3 19V14H0Z" fill="#aaa"/></svg><div class="who">Council on Equity</div><div class="what">Swedish video closes the gender</div></div>

  <div class="contact-row abs" style="top:84px">ADDRESS<span>48 C BLOCK 210 FAIRHAVEN</span></div>
  <div class="contact-row abs" style="top:114px">PHONE<span>+1-555-014-2273</span></div>
  <div class="contact-row abs" style="top:144px">EMAIL<span><a>info@torvimbly.com</a></span></div>
</footer>
<div class="btn-contact abs">CONTACT US<i>›</i></div>

<div class="bottom-bar abs">
  <nav class="bottom-nav abs">HOME &nbsp; · &nbsp; BY THE NUMBERS &nbsp; · &nbsp; WHO WE ARE &nbsp; · &nbsp; BLOG</nav>
  <div class="copyright abs">Copyright © 2014 Torvimbly. All rights reserved.</div>
</div>

</body>
</html>
```